依頼概要
■ 依頼の目的/概要

育毛剤・シャンプーのランキングサイトのデザインをお願い致します。

■ デザインへの要望

・イメージ画像として人間(できれば女性)の写真もしくは、イラストを使用してください。
・ランキングの順位と商品の特徴(写真や文字)をメインに強調したデザインにしてください。
・サイトを訪れた際に育毛剤・シャンプーのランキングサイトであることがわかるようにしてください。
・ランキングの上位3件ほどがはっきりと見えるようにしてください。
・ランキングサイトの参考として以下に、いくつか参考URLを記載しておきます。
・http://xn--5tvb61qmza.net/
・http://xn--5tvb61qkwp.com/
・http://www.zjaplitq.org/
・http://www.velparinsoda-listing.com/
・http://dobrasiel.t-hopa.net/

■ 納品ファイルの希望

フォトショップ形式(.psd形式)でお願い致します。

■ 利用用途

主に育毛剤・シャンプーのランキングサイトに使用させて頂きます。

■ 進め方

弊社の希望するイメージに近い提案を1つ(場合によって複数)選択させて頂きます。希望に近づけるために、修正要望を個別にさせて頂くこともあります。コンペ方式のため、修正後に当選されない場合も、どうかご了承ください。

■ その他/注意点

選択させて頂いたデザインの著作権(財産権)等の扱いはWispoll利用規約に従い、弊社に譲渡をお願いします。フォントや画像素材などを利用する場合は上記利用用途に使用できることを確認し、第三者の知的財産権等に注意して下さい。
補足:
今回はサイトのトップページのデザインのみでも結構です。

トップページに必要な内容ですが、
サイトを訪れた際に育毛剤ランキングへのリンクと、シャンプーランキングへのリンクとランキングの上位3位までは、表示できるようにして下さい。
(最初に表示されるのは育毛剤ランキングでお願い致します)

トップページの項目としては以下のようにお願い致します。
ナビゲーション(育毛剤ランキングへのリンクとシャンプーランキングへのリンク), 商品名, 商品の特徴を表した一文(※), 価格, 容量, 男女兼用かどうか, 評判(☆を使うなどわかりやすく), 販売サイトへのリンク

サイトのロゴや基調となる色の指定は、暖色系を基調としてください。

※商品の特徴を表した一文の例文と致しましては、「発毛率No.1の育毛サプリメント!」や「発毛率96%、平均1~2ヶ月の発毛スピード!」また、「30日で満足できないなら全額返金!」などです。
■ 選んだ理由

今回mibedutさんの提案を当選とさせて頂いた理由と致しましては、
要望に対してイメージ通りの提案をして下さったことです。

修正依頼に対しても誠意をもって応じて下さったので、
この提案を当選とさせて頂きました。

■ 提案者全員へのお礼・コメント

皆様、ご提案ありがとうございました。
弊社としましても非常に選考に苦労いたしました。

落選された方には残念な結果にはなったのですが、
今後とも機会がございましたら、よろしくお願い致します。

```html
<!DOCTYPE html>
<html lang="ja">
<head>
<meta charset="utf-8">
<title>育毛剤&amp;シャンプーのランキングサイト</title>
<link href="https://fonts.googleapis.com/css2?family=Noto+Sans+JP:wght@400;700&family=Noto+Serif+JP:wght@700&display=swap" rel="stylesheet">
<style>
:root{
  --red:#c8121c;
  --red-dark:#9c0a12;
  --red-light:#e24a4f;
  --pink:#f7dede;
  --gold:#d49a12;
  --orange:#f08a12;
  --yellow:#ffe36a;
  --grey:#eeeeee;
  --line:#d9d9d9;
  --text:#333333;
  --muted:#777777;
  --bg:#ebebeb;
}
*{box-sizing:border-box;margin:0;padding:0}
html,body{width:1200px;height:2628px;overflow:hidden}
body{background:linear-gradient(90deg,#d9d9d9,var(--bg) 60px,var(--bg) 1140px,#d9d9d9);font-family:"Noto Sans JP",sans-serif;color:var(--text);font-size:15px}
.page{width:1120px;height:2628px;margin:0 auto;background:#fff;position:relative;box-shadow:0 0 12px rgba(0,0,0,.15)}
.site-header{height:250px;position:relative;border-left:18px solid var(--red);overflow:hidden;background:linear-gradient(180deg,#fff 60%,#fbeeee)}
.site-title{position:absolute;left:40px;top:50px;font-family:"Noto Serif JP",serif;font-size:46px;color:var(--text);line-height:1.2}
.site-title small{display:block;font-size:30px}
.site-title em{font-style:normal;color:var(--red)}
.header-watermark{position:absolute;left:360px;top:120px;font-family:"Noto Serif JP",serif;font-size:72px;color:#f1d4d4;letter-spacing:2px}
.hero{position:absolute;left:560px;top:0;width:270px;height:250px;background:linear-gradient(160deg,#f3e4dc,#c99a86 60%,#7a4a3e)}
.header-note{position:absolute;left:850px;top:40px;width:240px;font-size:15px;line-height:1.6;color:var(--text)}
.global-nav{height:62px;background:linear-gradient(180deg,var(--red-light),var(--red) 50%,var(--red-dark));display:flex}
.global-nav a{flex:1;display:flex;align-items:center;justify-content:center;color:#fff;font-size:26px;font-weight:700;text-decoration:none;border-right:2px solid rgba(255,255,255,.4)}
.global-nav a:first-child{background:rgba(255,255,255,.12)}
.breadcrumb-row{display:flex;justify-content:space-between;padding:14px 40px;font-size:13px;color:var(--muted);border-bottom:1px solid var(--line)}
.breadcrumb-row .date{color:var(--red)}
.layout{display:flex;padding:24px 30px 0 40px;gap:30px}
.sidebar{width:260px;flex:none}
.side-menu{background:#f4f4f4;border:1px solid var(--line);margin-bottom:40px;padding-bottom:12px}
.side-menu h3{font-size:15px;padding:10px 14px;border-bottom:2px solid var(--red);color:var(--text)}
.side-menu li{list-style:none;font-size:14px;padding:8px 20px;border-bottom:1px dotted #ccc;color:var(--muted)}
.ranking{width:760px}
.rank-item{height:412px}
.rank-head{height:52px;display:flex;align-items:center;gap:10px;font-family:"Noto Serif JP",serif;font-size:30px;color:var(--gold)}
.rank-head .place{font-size:40px;color:var(--red)}
.rank-card{height:345px;border:2px solid var(--red);background:#fff}
.card-bar{height:42px;display:flex;justify-content:space-between;align-items:center;padding:0 14px;background:linear-gradient(180deg,var(--red-light),var(--red-dark));color:#fff}
.card-bar h2{font-size:20px}
.card-bar .catch{color:var(--yellow);font-weight:700;font-size:16px}
.card-body{display:flex;padding:16px;gap:20px}
.product-photo{width:180px;height:270px;flex:none;border:1px solid var(--line)}
.card-info{flex:1}
.spec{width:100%;border-collapse:collapse;font-size:14px;text-align:center;margin-bottom:14px}
.spec th{background:var(--grey);font-weight:400;padding:5px;border:1px solid var(--line)}
.spec td{padding:6px;border:1px solid var(--line)}
.spec .stars{color:var(--orange);letter-spacing:1px}
.desc{font-size:14px;line-height:1.8;height:128px;overflow:hidden}
.desc b{color:var(--red)}
.actions{display:flex;justify-content:flex-end;gap:14px;margin-top:16px}
.btn{display:inline-block;width:170px;padding:9px 0;text-align:center;border-radius:4px;font-size:14px;font-weight:700;text-decoration:none}
.btn-detail{background:linear-gradient(#fafafa,#ddd);border:1px solid #bbb;color:var(--text)}
.btn-official{background:linear-gradient(#ffb347,var(--orange));color:#fff;border:1px solid #d8720a}
.pager{display:flex;justify-content:flex-end;gap:12px;margin-top:8px}
.pager a{background:linear-gradient(var(--red-light),var(--red-dark));color:#fff;font-size:14px;padding:8px 22px;border-radius:4px;text-decoration:none}
.site-footer{position:absolute;bottom:0;left:0;right:0;height:70px;border-top:4px solid var(--red);display:flex;justify-content:space-between;align-items:center;padding:0 40px;font-size:13px;color:var(--muted);background:#f7f7f7}
.page-top{position:absolute;right:40px;bottom:80px;font-size:12px;color:var(--red)}
</style>
</head>
<body>
<div class="page">
  <header class="site-header">
    <h1 class="site-title"><em>育毛剤</em>&amp;<em>シャンプー</em>の<small>ランキングサイト</small></h1>
    <div class="header-watermark">Ranking</div>
    <div class="hero" role="img" aria-label="髪の美しい女性のイメージ写真"></div>
    <p class="header-note">話題の育毛剤と人気シャンプーを徹底比較。効果・価格・評判からランキング形式でご紹介します。</p>
  </header>
  <nav class="global-nav">
    <a href="#">○ 育毛剤の人気ランキング</a>
    <a href="#">○ シャンプーの人気ランキング</a>
  </nav>
  <div class="breadcrumb-row"><span>TOP &gt; 育毛剤ランキング &gt; 育毛剤人気ランキング</span><span class="date">育毛剤人気ランキング</span></div>
  <div class="layout">
    <aside class="sidebar">
      <div class="side-menu"><h3>育毛剤ランキング</h3><ul>
        <li>・ダミーダミーダミー</li><li>・ダミーダミーダミー</li><li>・ダミーダミーダミー</li><li>・ダミーダミーダミー</li><li>・ダミーダミーダミー</li><li>・ダミーダミーダミー</li><li>・ダミーダミーダミー</li><li>・ダミーダミーダミー</li></ul></div>
      <div class="side-menu"><h3>シャンプーランキング</h3><ul>
        <li>・ダミーダミーダミー</li><li>・ダミーダミーダミー</li><li>・ダミーダミーダミー</li><li>・ダミーダミーダミー</li><li>・ダミーダミーダミー</li><li>・ダミーダミーダミー</li><li>・ダミーダミーダミー</li><li>・ダミーダミーダミー</li></ul></div>
    </aside>
    <main class="ranking">
      <section class="rank-item">
        <div class="rank-head"><svg width="40" height="32" viewBox="0 0 40 32"><path d="M2 28 L5 6 L14 16 L20 2 L26 16 L35 6 L38 28 Z" fill="#d49a12"/></svg><span class="place">1</span>位</div>
        <div class="rank-card">
          <div class="card-bar"><h2>| R-7 育毛ミスト</h2><span class="catch">30日で満足できないなら全額返金!</span></div>
          <div class="card-body">
            <div class="product-photo" role="img" aria-label="白い育毛ミストのボトル" style="background:linear-gradient(#fff,#e8e8e8)"></div>
            <div class="card-info">
              <table class="spec"><tr><th>価格</th><th>容量</th><th>男女兼用</th><th>評判</th></tr><tr><td>¥5,040</td><td>120ml</td><td>○</td><td class="stars">★★★★★</td></tr></table>
              <p class="desc">頭皮環境を整える成分を配合し、<b>30日間の全額返金保証付き</b>で初めての方も安心。毎日のケアで抜け毛を防ぎ、健やかな髪の成長をしっかりサポートします。<b>多くの愛用者から高評価</b>を得ている人気の育毛剤です。</p>
              <div class="actions"><a class="btn btn-detail" href="#">» 商品詳細</a><a class="btn btn-official" href="#">» 公式サイトへ</a></div>
            </div>
          </div>
        </div>
      </section>
      <section class="rank-item">
        <div class="rank-head"><svg width="40" height="32" viewBox="0 0 40 32"><path d="M2 28 L5 6 L14 16 L20 2 L26 16 L35 6 L38 28 Z" fill="#a8a8a8"/></svg><span class="place">2</span>位</div>
        <div class="rank-card">
          <div class="card-bar"><h2>| ヘアライトプレミアム</h2><span class="catch">発毛率97%を誇るレーザー育毛器!</span></div>
          <div class="card-body">
            <div class="product-photo" role="img" aria-label="赤いレーザー育毛器" style="background:linear-gradient(#fff,#f0d0d0)"></div>
            <div class="card-info">
              <table class="spec"><tr><th>価格</th><th>容量</th><th>男女兼用</th><th>評判</th></tr><tr><td>¥45,000</td><td>-</td><td>○</td><td class="stars">★★★★☆</td></tr></table>
              <p class="desc">レーザーの光で頭皮を刺激し、<b>発毛率97%という高い実績</b>を持つ家庭用育毛器です。1回わずか数分のケアで手軽に続けられ、<b>医療機関でも採用される技術</b>を自宅で体感できます。</p>
              <div class="actions"><a class="btn btn-detail" href="#">» 商品詳細</a><a class="btn btn-official" href="#">» 公式サイトへ</a></div>
            </div>
          </div>
        </div>
      </section>
      <section class="rank-item">
        <div class="rank-head"><svg width="40" height="32" viewBox="0 0 40 32"><path d="M2 28 L5 6 L14 16 L20 2 L26 16 L35 6 L38 28 Z" fill="#b87333"/></svg><span class="place">3</span>位</div>
        <div class="rank-card">
          <div class="card-bar"><h2>| Kavo 育毛サプリメント</h2><span class="catch">フサフサが実感出来ないなら全額返金!</span></div>
          <div class="card-body">
            <div class="product-photo" role="img" aria-label="白い育毛サプリメントの容器" style="background:linear-gradient(#fff,#e6e6e6)"></div>
            <div class="card-info">
              <table class="spec"><tr><th>価格</th><th>容量</th><th>男女兼用</th><th>評判</th></tr><tr><td>¥11,000</td><td>180粒</td><td>○</td><td class="stars">★★★★☆</td></tr></table>
              <p class="desc"><b>体の内側から髪に栄養を届ける</b>育毛サプリメント。必要な成分をバランス良く配合し、毎日の食事で不足しがちな栄養を補います。<b>実感できなければ全額返金</b>なので安心です。</p>
              <div class="actions"><a class="btn btn-detail" href="#">» 商品詳細</a><a class="btn btn-official" href="#">» 公式サイトへ</a></div>
            </div>
          </div>
        </div>
      </section>
      <section class="rank-item">
        <div class="rank-head"><span class="place">4</span>位</div>
        <div class="rank-card">
          <div class="card-bar"><h2>| フロリア 薬用育毛</h2><span class="catch">発毛率96%を誇る育毛剤が大人気!</span></div>
          <div class="card-body">
            <div class="product-photo" role="img" aria-label="赤い箱と育毛剤のボトル" style="background:linear-gradient(#2a0a0a,#8a1a1a)"></div>
            <div class="card-info">
              <table class="spec"><tr><th>価格</th><th>容量</th><th>男女兼用</th><th>評判</th></tr><tr><td>¥5,040</td><td>120ml</td><td>○</td><td class="stars">★★★★☆</td></tr></table>
              <p class="desc">独自の浸透技術で有効成分を頭皮の奥まで届ける薬用育毛剤。<b>発毛率96%の実績</b>があり、平均1〜2ヶ月で変化を感じる方も多数。<b>男女問わず使える</b>やさしい処方です。</p>
              <div class="actions"><a class="btn btn-detail" href="#">» 商品詳細</a><a class="btn btn-official" href="#">» 公式サイトへ</a></div>
            </div>
          </div>
        </div>
      </section>
      <section class="rank-item">
        <div class="rank-head"><span class="place">5</span>位</div>
        <div class="rank-card">
          <div class="card-bar"><h2>| ルミナシャンプー</h2><span class="catch">効果がないなら全額返金保証!</span></div>
          <div class="card-body">
            <div class="product-photo" role="img" aria-label="白いシャンプーボトル" style="background:linear-gradient(#fff,#ececec)"></div>
            <div class="card-info">
              <table class="spec"><tr><th>価格</th><th>容量</th><th>男女兼用</th><th>評判</th></tr><tr><td>¥2,940</td><td>300ml</td><td>○</td><td class="stars">★★★☆☆</td></tr></table>
              <p class="desc">女性の髪と頭皮のために作られた<b>ノンシリコンのアミノ酸シャンプー</b>。洗うたびに頭皮をやさしく整え、ハリとコシのある髪へ導きます。<b>返金保証付き</b>で気軽に試せます。</p>
              <div class="actions"><a class="btn btn-detail" href="#">» 商品詳細</a><a class="btn btn-official" href="#">» 公式サイトへ</a></div>
            </div>
          </div>
        </div>
      </section>
      <div class="pager"><a href="#">» 1〜5位</a><a href="#">» 6〜10位</a><a href="#">» 11〜15位</a></div>
    </main>
  </div>
  <a class="page-top" href="#">▲ PAGE TOP</a>
  <footer class="site-footer"><span>育毛剤とは | 運営者情報 | お問い合わせ | サイトマップ</span><span>Copyright © 育毛剤&amp;シャンプーのランキングサイト All Rights Reserved.</span></footer>
</div>
</body>
</html>
```